Corporate-Design für Osteopathie-Praxis
Das Corporate Design war sehr gut, Änderungswünsche wurden zügig und exakt umgesetzt. Die Designerin stand auch nach der Siegerehrung immer zur Verfügung und hat weitere kleine Änderungen problemlos vorgenommen. Die Zusammenarbeit war immer angenehm und ist nur zu empfehlen.
Zielgruppe
Wir sind eine neue Osteopathie Praxis mit einem Klientel von Jung bis Alt. Vorwiegend etwas gut situiertere Personen. Es soll daher exklusiv aber auch hip sein, da unser Ziel darin besteht eine sehr moderne und edle Praxis aufzubauen.
Aufgabenstellung
Die Praxis soll den Namen „Lumra“ bekommen. Aus zwei Gründen;
die Praxis befindet sich an der Küste in Kiel. Ich möchte hier eine Verbindung zum Standort schaffen. Zweitens sind in dem Namen „Lumra“ meine Initialen MB sowie die Abkürzung für Osteopathie, ost. , vorhanden. Wenn man diese Ideen in dem Logo wiederfinden könnte, wäre es sehr schön. Die Farben blau, weiß, grau richten sich an den skandinavisch-maritimen Stil dem ich folgen möchte. Ich möchte hierbei aber klassisch (nicht verspielt wie zB mit einem Leuchtturm im Logo), etwas exklusiv und hip sein. Es darf aber auch nicht zu abstrakt sein, sodass auch ältere Kunden den Namen/das Logo lesen können

```html
<!DOCTYPE html>
<html lang="de">
<head>
<meta charset="utf-8">
<title>Lumra – Praxis für Osteopathie · Geschäftsausstattung</title>
<link rel="stylesheet" href="https://fonts.googleapis.com/css2?family=Montserrat:wght@300;400;500;700&display=swap">
<style>
  :root{
    --teal:#3f6a80;
    --steel:#8fa9b9;
    --mist:#c9d6df;
    --paper:#ffffff;
    --ink:#7c8c96;
    --ink-dark:#55656f;
    --stage:#f1f3f4;
    --edge:#dde3e7;
    --tint:#f3f6f8;
  }
  *{box-sizing:border-box;margin:0;padding:0}
  html,body{width:1200px;height:680px;overflow:hidden;background:var(--stage);font-family:"Montserrat",Arial,sans-serif;color:var(--ink)}
  .canvas{position:relative;width:1200px;height:680px}
  .piece{position:absolute;background:var(--paper);border:1px solid var(--edge);overflow:hidden}
  .band{position:absolute;left:0;width:100%}
  .brand{display:flex;flex-direction:column;align-items:center;line-height:1}
  .brand-name{font-weight:400;color:var(--teal);letter-spacing:.04em}
  .brand-sub{font-weight:700;color:var(--teal);letter-spacing:.04em;margin-top:3px}
  .tiny{font-size:4.6px;line-height:1.55;color:var(--ink)}

  /* vertical business card – front */
  .card-v-front{left:34px;top:12px;width:138px;height:228px;background:var(--mist)}
  .card-v-front .top{top:0;height:70px;background:var(--paper)}
  .card-v-front .rule{top:70px;height:4px;background:var(--teal)}
  .card-v-front .brand{position:absolute;left:16px;top:22px;align-items:flex-start}
  .card-v-front .brand-name{font-size:24px}
  .card-v-front .brand-sub{font-size:5px}
  .card-v-front .person{position:absolute;right:12px;top:96px;text-align:right;color:var(--teal);font-size:9.4px;line-height:1.35;font-weight:400}
  .card-v-front .contact{position:absolute;right:12px;top:136px;text-align:right;font-size:4.8px;line-height:1.8;color:var(--ink-dark)}
  .card-v-front .web{position:absolute;right:12px;bottom:14px;font-size:6.4px;color:var(--ink-dark)}

  /* vertical business card – back */
  .card-v-back{left:34px;top:276px;width:138px;height:232px;background:var(--teal)}
  .card-v-back .top{top:0;height:68px;background:var(--paper)}
  .card-v-back .rule{top:68px;height:3px;background:var(--steel)}
  .card-v-back .brand{position:absolute;left:16px;top:12px;align-items:flex-start}
  .card-v-back .brand-name{font-size:24px}
  .card-v-back .brand-sub{font-size:5px}
  .card-v-back .claim{position:absolute;right:10px;top:112px;text-align:right;color:var(--paper);font-size:8px;line-height:1.6}
  .card-v-back .claim b{font-style:italic}
  .card-v-back .note{position:absolute;right:10px;top:180px;text-align:right;color:var(--mist);font-size:5px;line-height:1.6}

  /* letterheads */
  .letter{top:36px;width:250px;height:446px}
  .letter-a{left:206px}
  .letter-b{left:846px}
  .letter .brand{position:absolute;right:22px;top:16px}
  .letter .brand-name{font-size:22px}
  .letter .brand-sub{font-size:5px}
  .letter .brand-web{font-size:3.6px;color:var(--ink);margin-top:3px}
  .letter-b .brand{right:auto;left:50%;transform:translateX(-50%)}
  .letter .body{position:absolute;left:18px;right:26px;top:102px}
  .letter-b .body{left:30px;right:28px}
  .letter .body p{margin-bottom:14px}
  .letter .subject{margin-bottom:16px}
  .letter ul{list-style:none;margin:0 0 18px}
  .letter li{position:relative;padding-left:12px;margin-bottom:6px}
  .letter li::before{content:"";position:absolute;left:2px;top:2px;width:4px;height:4px;border-radius:50%;background:var(--teal)}
  .letter .sign{margin-top:20px}
  .letter-b .sign{text-align:right}
  .letter .fold{position:absolute;left:-1px;top:128px;width:8px;height:1px;background:var(--ink)}
  .letter-a .base{bottom:0;height:70px;background:var(--tint);border-top:1px solid var(--edge)}
  .letter-a .footer{position:absolute;right:22px;bottom:18px;text-align:right;font-size:3.6px;line-height:1.7;color:var(--ink-dark)}
  .letter-b .base{bottom:14px;height:6px;background:var(--steel)}
  .letter-b .base-line{bottom:8px;height:1px;background:var(--mist)}
  .letter-b .footer{position:absolute;left:22px;right:22px;bottom:48px;display:flex;justify-content:space-between;font-size:4.2px;line-height:1.5;color:var(--ink-dark);text-align:center}
  .letter-b .footer div{display:flex;flex-direction:column;align-items:center;gap:3px}
  .letter-b .footer svg{width:8px;height:8px}

  /* horizontal business cards */
  .card-h-front{left:590px;top:98px;width:228px;height:150px}
  .card-h-front .brand{position:absolute;left:0;right:0;top:28px}
  .card-h-front .brand-name{font-size:46px;font-weight:300}
  .card-h-front .brand-sub{font-size:10px;margin-top:4px}
  .card-h-front .web{position:absolute;left:0;right:0;bottom:24px;text-align:center;font-size:8px;color:var(--mist)}
  .card-h-back{left:590px;top:274px;width:228px;height:150px}
  .card-h-back .brand{position:absolute;left:20px;top:14px;align-items:flex-start}
  .card-h-back .brand-name{font-size:15px}
  .card-h-back .brand-sub{font-size:3.4px;margin-top:2px}
  .card-h-back .person{position:absolute;right:20px;top:42px;text-align:right;color:var(--teal);font-size:8.4px;line-height:1.3;font-variant:small-caps;letter-spacing:.04em}
  .card-h-back .contact{position:absolute;right:14px;top:72px;font-size:4.8px;line-height:2.15;color:var(--ink)}
  .card-h-back .contact div{display:flex;justify-content:flex-end;align-items:center;gap:5px}
  .card-h-back .contact svg{width:6px;height:6px}

  /* envelopes */
  .env{background:var(--paper)}
  .env-a-front{left:154px;top:526px;width:126px;height:126px}
  .env-a-front .brand{position:absolute;left:0;right:0;top:12px}
  .env-a-front .brand-name{font-size:15px}
  .env-a-front .brand-sub{font-size:3.4px;margin-top:2px}
  .env-a-front .base{bottom:18px;height:4px;background:var(--steel)}
  .window{position:absolute;border:1px solid var(--edge);background:#f6f8f9;border-radius:3px}
  .env-a-front .window{left:14px;top:50px;width:58px;height:36px}
  .env-a-back{left:304px;top:504px;width:235px;height:170px}
  .env-a-back .base{bottom:22px;height:6px;background:var(--steel)}
  .env-a-back .web{position:absolute;right:18px;bottom:34px;font-size:4.4px;color:var(--ink)}
  .env-b-front{left:648px;top:528px;width:250px;height:126px}
  .env-b-front .brand{position:absolute;left:28px;top:18px;align-items:flex-start}
  .env-b-front .brand-name{font-size:22px}
  .env-b-front .brand-sub{font-size:4.6px}
  .env-b-front .window{left:28px;top:64px;width:82px;height:42px}
  .env-b-front .web{position:absolute;right:24px;top:86px;font-size:6px;font-weight:700;color:var(--teal)}
  .env-b-back{left:918px;top:510px;width:178px;height:160px}
  .flap{position:absolute;left:0;top:0;width:100%;height:100%}
</style>
</head>
<body>
<main class="canvas">

  <!-- Vertical card, front -->
  <section class="piece card-v-front">
    <div class="band top"></div>
    <div class="band rule"></div>
    <div class="brand"><span class="brand-name">Lumra</span><span class="brand-sub">PRAXIS FÜR OSTEOPATHIE</span></div>
    <div class="person">Dr. med.<br>Vorname Nachname</div>
    <div class="contact">Hafenweg 12, 24103 Kiel<br>Telefon 0431 / 556 210<br>Mobil 0171 / 482 3390<br>E-Mail info@praxis-lumra-kiel.de</div>
    <div class="web">www.praxis-lumra-kiel.de</div>
  </section>

  <!-- Vertical card, back -->
  <section class="piece card-v-back">
    <div class="band top"></div>
    <div class="band rule"></div>
    <div class="brand"><span class="brand-name">Lumra</span><span class="brand-sub">PRAXIS FÜR OSTEOPATHIE</span></div>
    <p class="claim">Lassen Sie meine Hände<br>und Ihren Körper<br>ein <b>Gespräch</b> führen!</p>
    <p class="note">Terminvereinbarung<br>bitte telefonisch<br>oder per E-Mail</p>
  </section>

  <!-- Letterhead A -->
  <section class="piece letter letter-a">
    <span class="fold"></span>
    <div class="brand"><span class="brand-name">Lumra</span><span class="brand-sub">PRAXIS FÜR OSTEOPATHIE</span><span class="brand-web">www.praxis-lumra-kiel.de</span></div>
    <div class="body tiny">
      <p class="subject">Betreff</p>
      <p>Sehr geehrte Damen und Herren,</p>
      <p>Vielen Dank für Ihre Anfrage. Gerne bestätigen wir Ihren Termin in unserer Praxis und freuen uns auf Ihren Besuch.</p>
      <ul>
        <li>Bitte bringen Sie bequeme Kleidung und vorhandene Befunde mit.</li>
        <li>Planen Sie für die erste Behandlung etwa eine Stunde ein.</li>
      </ul>
      <p>Sollten Sie den Termin nicht wahrnehmen können, sagen Sie bitte mindestens einen Tag vorher ab. Wir melden uns gern bei Fragen.</p>
      <p class="sign">Unterschrift<br>Dr. med.</p>
    </div>
    <div class="band base"></div>
    <div class="footer">Hafenweg 12 · 24103 Kiel<br>Telefon 0431 / 556 210 · Mobil 0171 / 482 3390<br>info@praxis-lumra-kiel.de<br>Bankverbindung Kieler Bank<br>Steuernummer 00/000/00000</div>
  </section>

  <!-- Horizontal card, front -->
  <section class="piece card-h-front">
    <div class="brand"><span class="brand-name">Lumra</span><span class="brand-sub">PRAXIS FÜR OSTEOPATHIE</span></div>
    <div class="web">www.praxis-lumra-kiel.de</div>
  </section>

  <!-- Horizontal card, back -->
  <section class="piece card-h-back">
    <div class="brand"><span class="brand-name">Lumra</span><span class="brand-sub">PRAXIS FÜR OSTEOPATHIE</span></div>
    <div class="person">Dr. med.<br>Vorname Nachname</div>
    <div class="contact">
      <div>Telefon 0431 / 556 210 <svg viewBox="0 0 10 10" aria-hidden="true"><path d="M2 1 L4 1 L5 3.5 L3.8 4.5 C4.4 5.8 5 6.4 6.2 7 L7 5.8 L9 6.8 L9 9 C5 9 1 5 1 1 Z" fill="var(--teal)"/></svg></div>
      <div>Mobil 0171 / 482 3390 <svg viewBox="0 0 10 10" aria-hidden="true"><rect x="3" y="0.5" width="4" height="9" rx="1" fill="var(--teal)"/></svg></div>
      <div>Hafenweg 12, 24103 Kiel <svg viewBox="0 0 10 10" aria-hidden="true"><path d="M5 0.5 C7.2 0.5 8.5 2 8.5 3.8 C8.5 6 5 9.5 5 9.5 C5 9.5 1.5 6 1.5 3.8 C1.5 2 2.8 0.5 5 0.5 Z" fill="var(--teal)"/><circle cx="5" cy="3.8" r="1.2" fill="#fff"/></svg></div>
      <div>E-Mail info@praxis-lumra-kiel.de <svg viewBox="0 0 10 10" aria-hidden="true"><rect x="0.5" y="2" width="9" height="6" fill="var(--teal)"/><path d="M0.5 2 L5 5.5 L9.5 2" fill="none" stroke="#fff" stroke-width=".8"/></svg></div>
    </div>
  </section>

  <!-- Letterhead B -->
  <section class="piece letter letter-b">
    <span class="fold"></span>
    <div class="brand"><span class="brand-name">Lumra</span><span class="brand-sub">PRAXIS FÜR OSTEOPATHIE</span></div>
    <div class="body tiny">
      <p class="subject">Betreff</p>
      <p>Sehr geehrte Damen und Herren,</p>
      <p>Vielen Dank für Ihre Anfrage. Gerne bestätigen wir Ihren Termin in unserer Praxis und freuen uns auf Ihren Besuch.</p>
      <ul>
        <li>Bitte bringen Sie bequeme Kleidung und vorhandene Befunde mit.</li>
        <li>Planen Sie für die erste Behandlung etwa eine Stunde ein.</li>
      </ul>
      <p>Sollten Sie den Termin nicht wahrnehmen können, sagen Sie bitte mindestens einen Tag vorher ab. Wir melden uns gern bei Fragen.</p>
      <p class="sign">Unterschrift<br>Dr. med.</p>
    </div>
    <div class="footer">
      <div><svg viewBox="0 0 10 10" aria-hidden="true"><path d="M5 0.5 C7.2 0.5 8.5 2 8.5 3.8 C8.5 6 5 9.5 5 9.5 C5 9.5 1.5 6 1.5 3.8 C1.5 2 2.8 0.5 5 0.5 Z" fill="var(--steel)"/><circle cx="5" cy="3.8" r="1.2" fill="#fff"/></svg><span>24103 Kiel<br>Hafenweg 12</span></div>
      <div><svg viewBox="0 0 10 10" aria-hidden="true"><path d="M2 1 L4 1 L5 3.5 L3.8 4.5 C4.4 5.8 5 6.4 6.2 7 L7 5.8 L9 6.8 L9 9 C5 9 1 5 1 1 Z" fill="var(--steel)"/></svg><span>Telefon 0431 / 556 210<br>Mobil 0171 / 482 3390</span></div>
      <div><svg viewBox="0 0 10 10" aria-hidden="true"><rect x="0.5" y="2" width="9" height="6" fill="var(--steel)"/><path d="M0.5 2 L5 5.5 L9.5 2" fill="none" stroke="#fff" stroke-width=".8"/></svg><span>info@praxis-lumra-kiel.de<br>www.praxis-lumra-kiel.de</span></div>
    </div>
    <div class="band base"></div>
    <div class="band base-line"></div>
  </section>

  <!-- Envelope A, front -->
  <section class="piece env env-a-front">
    <div class="brand"><span class="brand-name">Lumra</span><span class="brand-sub">PRAXIS FÜR OSTEOPATHIE</span></div>
    <div class="window"></div>
    <div class="band base"></div>
  </section>

  <!-- Envelope A, back -->
  <section class="piece env env-a-back">
    <svg class="flap" viewBox="0 0 235 170" preserveAspectRatio="none" aria-hidden="true">
      <path d="M0 0 L117 70 L235 0" fill="none" stroke="var(--edge)" stroke-width="1"/>
    </svg>
    <div class="web">www.praxis-lumra-kiel.de</div>
    <div class="band base"></div>
  </section>

  <!-- Envelope B, front -->
  <section class="piece env env-b-front">
    <div class="brand"><span class="brand-name">Lumra</span><span class="brand-sub">PRAXIS FÜR OSTEOPATHIE</span></div>
    <div class="window"></div>
    <div class="web">www.praxis-lumra-kiel.de</div>
  </section>

  <!-- Envelope B, back -->
  <section class="piece env env-b-back">
    <svg class="flap" viewBox="0 0 178 160" preserveAspectRatio="none" aria-hidden="true">
      <path d="M0 0 L89 60 L178 0" fill="none" stroke="var(--edge)" stroke-width="1"/>
    </svg>
  </section>

</main>
</body>
</html>
```